LETTERHEAD & ENVELOPE: eye-catching stationary design for our custom office furniture business

Our company recently rebranded and we are in need of new stationary. Specifically, we need branded letterhead for standard paper size (8.5” x 11”), and matching envelopes, size: #9.

All designs should incorporate our brand colors, brand typeface, and logo. Please view attached brand guidelines document for brand colors, and brand description.

Letterhead: 8.5” x 11” Must include CoralvexKTN Logo, Dorrit Falke Certified Dealer Logo, mailing address, phone number, website, and email address.

Envelope: 9.5” x 4.125” Must include CoralvexKTN Logo, mailing address, and Dorrit Falke Certified Dealer Logo.

Attached files include:

```html
<!DOCTYPE html>
<html lang="en">
<head>
<meta charset="utf-8">
<title>CoralvexKTN Stationery – Letterhead &amp; Envelope</title>
<link href="https://fonts.googleapis.com/css2?family=Poppins:wght@500;600&family=Raleway:wght@300;400;500&family=Fira+Sans:wght@400;600&family=Roboto+Condensed:wght@400&display=swap" rel="stylesheet">
<style>
:root{
  --board:#67686a;
  --paper:#ffffff;
  --brand:#4f7a6a;
  --brand-dark:#5a7d6d;
  --navy:#2f5b7a;
  --ink:#3b3b3b;
  --dealer:#e2402a;
  --sig:#b9c4c0;
}
*{margin:0;padding:0;box-sizing:border-box}
html,body{width:1200px;height:1200px;overflow:hidden;background:var(--board)}
.canvas{position:relative;width:1200px;height:1200px;background:var(--board);font-family:"Raleway",sans-serif}
.abs{position:absolute;white-space:nowrap}

/* spec labels */
.spec{color:#fff;font-family:"Poppins",sans-serif;font-weight:600}
.spec-title{left:621px;top:16px;font-size:32px}
.spec-product{font-size:37px}
.spec-line{font-size:22px;font-weight:500;line-height:35px}

/* sheets */
.sheet{position:absolute;background:var(--paper);overflow:hidden}
.letterhead{left:46px;top:69px;width:527px;height:681px}
.envelope{left:46px;top:809px;width:819px;height:338px}

.brand-mark{display:flex;align-items:center;position:absolute}
.brand-dot{border-radius:50%;background:var(--brand);flex:none}
.brand-name{font-family:"Raleway",sans-serif;font-weight:400;color:var(--brand);letter-spacing:.2px}

.divider{position:absolute;width:1px;background:#8aa59b}
.contact{position:absolute;font-family:"Fira Sans",sans-serif;color:var(--ink);white-space:nowrap}
.contact b{font-weight:600;color:var(--brand)}
.company{font-family:"Fira Sans",sans-serif;font-weight:600;color:var(--brand);position:absolute;white-space:nowrap}

.dealer{position:absolute;display:flex;align-items:center}
.dealer-dot{border-radius:50%;background:var(--dealer);flex:none}
.dealer-name{font-family:"Roboto Condensed",sans-serif;color:var(--dealer);white-space:nowrap}

.corner{position:absolute;right:0;bottom:0}

/* letter body */
.recipient{position:absolute;left:31px;top:146px;font-family:"Poppins",sans-serif;color:var(--ink)}
.recipient .to{font-size:7px}
.recipient .name{font-size:11px;color:var(--navy);font-weight:500;line-height:14px}
.recipient .meta{font-size:7.5px;line-height:11px}
.date{position:absolute;right:32px;top:163px;font-family:"Poppins",sans-serif;font-size:7.5px;color:var(--ink)}
.date b{color:var(--navy);font-weight:600}
.body{position:absolute;left:31px;top:211px;width:463px;font-size:7.6px;line-height:12.9px;color:#4a4a4a;text-align:justify}
.body p{margin-bottom:12.9px}
.signature{position:absolute;left:31px;top:471px;width:140px;height:22px;background:linear-gradient(90deg,var(--sig),#e3e8e6)}
.signer{position:absolute;left:31px;top:505px;font-family:"Poppins",sans-serif}
.signer .name{font-size:11px;font-weight:500;color:var(--navy);letter-spacing:.4px}
.signer .role{font-size:8px;font-weight:600;color:#222}
</style>
</head>
<body>
<main class="canvas">

  <div class="abs spec spec-title">Mockup - 1</div>
  <div class="abs spec spec-product" style="left:617px;top:80px">Letterhead- 8.5”X11”</div>
  <div class="abs spec spec-line" style="left:620px;top:132px">Color Mode: CMYK<br>High Quality PDF, EPS, JPG, PNG &amp; TIFF</div>

  <div class="abs spec spec-product" style="left:614px;top:684px">Envelope- 9.5”X4.125”</div>
  <div class="abs spec spec-line" style="left:884px;top:818px">Color Mode: CMYK<br>High Quality PDF, EPS,<br>JPG, PNG &amp; TIFF</div>

  <!-- Letterhead -->
  <section class="sheet letterhead">
    <div class="brand-mark" style="left:31px;top:25px">
      <span class="brand-dot" style="width:32px;height:32px"></span>
      <span class="brand-name" style="font-size:24px;margin-left:11px">CoralvexKTN</span>
    </div>
    <div class="divider" style="left:274px;top:21px;height:40px"></div>
    <div class="contact" style="left:292px;top:26px;font-size:6.4px;line-height:12px">
      <b>P:</b> 555.214.0187<br><b>W:</b> www.coralvexktn.com<br><b>E:</b> hello@coralvexktn.com
    </div>
    <div class="divider" style="left:382px;top:21px;height:40px"></div>
    <div class="company" style="left:399px;top:21px;font-size:13px">CoralvexKTN</div>
    <div class="contact" style="left:399px;top:38px;font-size:6px;line-height:12px">418 Larkmoor Ave, Suite 120<br>Eastbrook, OR 97015</div>

    <div class="recipient">
      <div class="to">To</div>
      <div class="name">Miles Arden</div>
      <div class="meta"><b>CEO, BRIGHTFOLD</b><br><b>W:</b> www.brightfold.com</div>
    </div>
    <div class="date"><b>Date:</b> 24-03-2018</div>

    <div class="body">
      <p>Lorem ipsum dolor sit amet, consectetur adipiscing elit. Pellentesque dictum, ante non ullamcorp er convallis, nunc quam blandit metus, ac mollis eros felis a orci. Donec congue, mauris ut pulvinar lobortis, dolor massa feugiat nisi, at tincidunt metus leo vel elit. Proin facilisis semper lobortis. Vivamus augue purus, cursus quis urna non, accumsan pellentesque est. Nulla in iaculis magna, quis aliqu et ex. Cras efficitur metus eget purus euismod facilisis. Proin non metus tincidunt, auctor ipsum a, tempor mi.</p>
      <p>Nulla egestas vulputate risus, ut vestibulum diam commodo id. Mauris ornare libero eu erat portt itor ultrices. Proin sed lectus scelerisque ligula bibendum sagittis ac nec leo. Donec ac accumsan diam, et lobortis mauris.</p>
      <p>Nulla congue volutpat nisl ac lobortis. Integer dignissim interdum libero, quis feugiat velit pretium at. Phasellus sit amet libero rutrum, feugiat odio et, tempus purus. Cras ultricies, leo at fringilla solli cit udin, leo sapien placerat enim, a rutrum lorem enim ut tortor. Phasellus magna ante, cong ue maximus egestas sit amet, venenatis scelerisque felis.</p>
      <p>Nulla congue volutpat nisl ac lobortis. Integer dignissim interdum libero, quis feugiat velit pretium at. Phasellus sit amet libero rutrum, feugiat odio et, tempus purus. Cras ultricies, leo at fringilla solli cit udin, leo sapien placerat enim, a rutrum lorem enim ut tortor. Phasellus magna ante, cong ue maximus egestas sit amet, venenatis scelerisque felis.</p>
    </div>

    <div class="signature" role="img" aria-label="Handwritten signature"></div>
    <div class="signer">
      <div class="name">MILES ARDEN</div>
      <div class="role">Vice President</div>
    </div>

    <div class="dealer" style="left:31px;top:625px">
      <span class="dealer-dot" style="width:30px;height:30px"></span>
      <span class="dealer-name" style="font-size:14.5px;margin-left:9px">Dorrit Falke Certified Dealer</span>
    </div>

    <svg class="corner" width="133" height="101" viewBox="0 0 133 101" aria-hidden="true">
      <polygon points="0,101 133,101 133,0" fill="var(--brand-dark)"/>
    </svg>
  </section>

  <!-- Envelope -->
  <section class="sheet envelope">
    <div class="brand-mark" style="left:21px;top:34px">
      <span class="brand-dot" style="width:43px;height:43px"></span>
      <span class="brand-name" style="font-size:32px;margin-left:13px">CoralvexKTN</span>
    </div>
    <div class="contact" style="left:21px;top:105px;font-size:9.6px;line-height:17.6px">
      <b>P:</b> 555.214.0187<br><b>W:</b> www.coralvexktn.com<br><b>E:</b> hello@coralvexktn.com
    </div>
    <div class="divider" style="left:154px;top:101px;height:58px"></div>
    <div class="company" style="left:179px;top:98px;font-size:20px">CoralvexKTN</div>
    <div class="contact" style="left:179px;top:124px;font-size:9.6px;line-height:17.6px">418 Larkmoor Ave, Suite 120<br>Eastbrook, OR 97015</div>

    <div class="dealer" style="left:21px;top:290px">
      <span class="dealer-dot" style="width:32px;height:32px"></span>
      <span class="dealer-name" style="font-size:16.5px;margin-left:10px">Dorrit Falke Certified Dealer</span>
    </div>

    <svg class="corner" width="196" height="150" viewBox="0 0 196 150" aria-hidden="true">
      <polygon points="0,150 196,150 196,0" fill="var(--brand-dark)"/>
    </svg>
  </section>

</main>
</body>
</html>
```